Business Card Design Project

Want a modern business card.
Concern is that our email address is long and thus poses a design challenge.
Items like the company name can be omitted from text as it will be available via the logo.

Example:
Gerald Tunstall
President / CEO
Cell 555.304.1182
Office 555.617.2093
geraldt@korvantsolutionsgroup.example
www.korvantsolutionsgroup.example

Target Market(s)

Technical and executive level members of Information Technology companies in the Healthcare industry.

Industry/Entity Type

Business

Colors

Designer to choose colors to be used in the design.

Requirements
Nice to have
• Raised logo, but I am open.

```html
<!DOCTYPE html>
<html lang="en">
<head>
<meta charset="utf-8">
<title>Korvant Solutions Group – Business Card</title>
<link rel="stylesheet" href="https://fonts.googleapis.com/css2?family=Barlow:wght@400;500;600&family=Cinzel:wght@700&display=swap">
<style>
  :root {
    --stage: #3a3634;
    --card-white: #ffffff;
    --card-grey: #d9dadc;
    --ink: #2b2b2b;
    --rule: #a9abad;
    --navy: #243a7a;
    --blue-light: #1b86c9;
    --blue-mid: #0f6aab;
    --blue-dark: #155a8e;
    --back-top: #0a86c8;
    --back-bottom: #0a4f90;
    --charcoal: #26282b;
    --charcoal-light: #45484b;
    --icon-bg: #262626;
    --white: #ffffff;
  }
  * { box-sizing: border-box; margin: 0; padding: 0; }
  html, body { width: 1000px; height: 1200px; overflow: hidden; }
  body {
    background: var(--stage);
    font-family: "Barlow", sans-serif;
    position: relative;
  }
  .card {
    position: absolute;
    width: 723px;
    height: 424px;
    overflow: hidden;
  }
  .card svg.card-shapes { position: absolute; inset: 0; }

  /* Front */
  .card-front {
    left: 140px; top: 118px;
    background: linear-gradient(160deg, var(--card-white) 35%, var(--card-grey) 100%);
  }
  .wordmark {
    position: absolute;
    right: 56px; top: 56px;
    text-align: right;
    font-family: "Barlow", sans-serif;
    font-weight: 600;
    color: var(--navy);
    line-height: 1;
  }
  .wordmark .wordmark-main { display: block; font-size: 42px; letter-spacing: 1px; }
  .wordmark .wordmark-sub { display: block; font-size: 20px; letter-spacing: 1px; margin-top: 4px; }
  .holder-name {
    position: absolute; left: 58px; top: 155px;
    font-size: 28px; font-weight: 600; color: var(--ink);
  }
  .name-rule {
    position: absolute; left: 58px; right: 0; top: 197px;
    height: 1px; background: var(--rule);
  }
  .holder-title {
    position: absolute; left: 58px; top: 206px;
    font-size: 21px; font-weight: 400; color: var(--ink);
  }
  .contact {
    position: absolute;
    display: flex; align-items: center; gap: 9px;
    color: var(--ink);
  }
  .contact .icon {
    width: 32px; height: 32px; border-radius: 50%;
    background: var(--icon-bg);
    display: flex; align-items: center; justify-content: center;
    flex: none;
  }
  .contact-phone { font-size: 21px; font-weight: 600; }
  .contact-web { font-size: 16px; font-weight: 400; }
  .contact-cell { left: 58px; top: 255px; }
  .contact-office { left: 389px; top: 255px; }
  .contact-email { left: 58px; top: 301px; }
  .contact-site { left: 389px; top: 301px; }

  /* Back */
  .card-back {
    left: 125px; top: 638px;
    height: 422px;
    background: radial-gradient(ellipse 70% 80% at 50% 20%, var(--back-top), var(--back-bottom));
  }
  .back-wordmark {
    position: absolute; left: 0; right: 0; top: 150px;
    text-align: center;
    font-weight: 600; color: var(--white); line-height: 1;
  }
  .back-wordmark .wordmark-main { display: block; font-size: 54px; letter-spacing: 2px; }
  .back-wordmark .wordmark-sub { display: block; font-size: 25px; letter-spacing: 2px; margin-top: 6px; }
  .back-url {
    position: absolute; left: 0; right: 0; top: 248px;
    text-align: center; color: var(--white);
    font-size: 22px; letter-spacing: 1px;
  }
</style>
</head>
<body>

<section class="card card-front" aria-label="Business card front">
  <svg class="card-shapes" width="723" height="424" viewBox="0 0 723 424" aria-hidden="true">
    <defs>
      <linearGradient id="frontBand" x1="0" y1="0" x2="1" y2="0">
        <stop offset="0" stop-color="var(--blue-light)"/>
        <stop offset="1" stop-color="var(--blue-dark)"/>
      </linearGradient>
    </defs>
    <rect class="tab-dark" x="-10" y="42" width="45" height="208" rx="6" fill="var(--blue-dark)"/>
    <rect class="tab-light" x="-10" y="119" width="33" height="208" rx="6" fill="var(--blue-light)"/>
    <rect class="tab-right" x="688" y="35" width="45" height="109" rx="8" fill="var(--blue-light)"/>
    <path class="band-light" d="M258,424 C260,388 292,365 335,365 H723 V424 Z" fill="url(#frontBand)"/>
    <path class="band-dark" d="M0,390 H415 C440,390 455,405 457,424 H0 Z" fill="var(--blue-dark)"/>
  </svg>

  <div class="wordmark">
    <span class="wordmark-main">KORVANT</span>
    <span class="wordmark-sub">SOLUTIONS GROUP</span>
  </div>

  <h1 class="holder-name">Gerald Tunstall</h1>
  <div class="name-rule"></div>
  <p class="holder-title">President / CEO</p>

  <div class="contact contact-cell">
    <span class="icon">
      <svg width="14" height="18" viewBox="0 0 14 18" aria-hidden="true"><rect x="2" y="1" width="10" height="16" rx="2" fill="none" stroke="#fff" stroke-width="1.8"/><circle cx="7" cy="14" r="1" fill="#fff"/></svg>
    </span>
    <span class="contact-phone">555.304.1182</span>
  </div>
  <div class="contact contact-office">
    <span class="icon">
      <svg width="16" height="16" viewBox="0 0 24 24" aria-hidden="true"><path fill="#fff" d="M6.6 10.8a15.1 15.1 0 0 0 6.6 6.6l2.2-2.2a1 1 0 0 1 1-.25 11.4 11.4 0 0 0 3.6.57 1 1 0 0 1 1 1V20a1 1 0 0 1-1 1A17 17 0 0 1 3 4a1 1 0 0 1 1-1h3.5a1 1 0 0 1 1 1c0 1.25.2 2.45.57 3.57a1 1 0 0 1-.25 1z"/></svg>
    </span>
    <span class="contact-phone">555.617.2093</span>
  </div>
  <div class="contact contact-email">
    <span class="icon">
      <svg width="17" height="13" viewBox="0 0 17 13" aria-hidden="true"><rect x="0.5" y="0.5" width="16" height="12" fill="#fff"/><path d="M0.5 0.5 L8.5 7 L16.5 0.5" fill="none" stroke="#262626" stroke-width="1.4"/></svg>
    </span>
    <span class="contact-web">geraldt@korvantsolutionsgroup.example</span>
  </div>
  <div class="contact contact-site">
    <span class="icon">
      <svg width="18" height="18" viewBox="0 0 18 18" aria-hidden="true"><g fill="none" stroke="#fff" stroke-width="1.4"><circle cx="9" cy="9" r="7.5"/><ellipse cx="9" cy="9" rx="3.3" ry="7.5"/><path d="M1.5 9 H16.5"/></g></svg>
    </span>
    <span class="contact-web">www.korvantsolutionsgroup.example</span>
  </div>
</section>

<section class="card card-back" aria-label="Business card back">
  <svg class="card-shapes" width="723" height="422" viewBox="0 0 723 422" aria-hidden="true">
    <defs>
      <linearGradient id="backBand" x1="0" y1="0" x2="1" y2="0">
        <stop offset="0" stop-color="var(--charcoal)"/>
        <stop offset="0.6" stop-color="var(--charcoal-light)"/>
        <stop offset="1" stop-color="var(--charcoal)"/>
      </linearGradient>
    </defs>
    <path class="band-upper" d="M0,362 H420 C447,362 463,374 467,389 H723 V422 H0 Z" fill="url(#backBand)"/>
    <path class="band-lower" d="M265,422 C270,401 292,389 325,389 H723 V422 Z" fill="var(--charcoal)"/>
  </svg>
  <div class="back-wordmark">
    <span class="wordmark-main">KORVANT</span>
    <span class="wordmark-sub">SOLUTIONS GROUP</span>
  </div>
  <p class="back-url">www.korvantsolutionsgroup.example</p>
</section>

</body>
</html>
```